Buch-Cover für Jahrbuch Merkurpfade
Das Design, das uns Wellenfalter geliefert hat, hat uns von Anfang an überzeugt. Kleine und geringfügige Änderungen wurden sehr schnell ausgeführt, die Kommunikation war immer sehr klar und freundlich. Insgesamt ein tolles Ergebnis, eine nette Arbeitsweise und schnell obendrein. Gerne wieder.
Zielgruppe
Der Verlag Falkenblatt bringt jedes Jahr ein Buch in der Reihe 'Merkurpfade' heraus. Angesprochen werden vermögende Privatkunden, die auf der Suche nach qualifizierten Informationen für ihre professionelle Geldanlage sind. Themen des Buches sind Vermögen, Aktien, Anleihen, Rohstoffe, Edelmetalle, nachhaltiges Investieren, Kryptowährungen, Kunst-Investments ... Die Anleger haben zwar Erfahrungen mit Geldanlage, sind aber keine Wissenschaftler oder sonstige Fachleute aus der Branche. Das Cover sollte daher nicht wirken wie das Lehrbuch eines BWL-Fachseminars.
Im vorigen Jahr haben wir beschlossen, das Konzept des Jahrbuchs umzustellen. Es ist nun dünner und geht konzentrierter auf die Inhalte ein. Wir haben die Anzahl der Beiträge reduziert und setzen nach dem Motto 'Klasse statt Masse' auf mehr hochqualitative Beiträge, die Anlegern präzise Analysen und innovative Strategien für ihre Geldanlage bieten. Mit dem neuen Cover wollen wir nun auch optisch die Neuausrichtung des Buches darstellen.
Das neue Buch trägt den Titel 'Der Zins kehrt langsam zurück' und soll im Oktober 2021 erscheinen. Redaktionsschluss ist Ende September.
Aufgabenstellung
Wir suchen ein zeitloses Design, das wir Jahr für Jahr wiederverwenden können. Der Stil sollte sachlich und modern sein. Darunter verstehen wir einen gleichmäßigen Farbeinsatz, klare geometrische Formen, ein Design das dem Text Raum lässt. Das Thema Geldanlage sollte im Cover widergespiegelt werden. Wir können uns gut geometrische Formen, die bildlich Luft und Raum verschaffen vorstellen. Unsere Farben (Blau, Rot siehe Logo und Cover Vorjahr) sollten in das Cover aufgenommen werden.
Auch für die Online-Vermarktung sollte sich das Cover gut eignen, sprich einen Wiedererkennungswert haben, dem Auge positiv auffallend sein und dem Betrachter schnell zeigen, worum es in diesem Sachbuch geht.
Was wir nicht wollen, sind Schnörkel oder kitschig verspielte Elemente. Auch ein einheitliches Farbprofil wäre uns wichtig, sprich allzu bunt sollte es nicht werden. Auch sollte es natürlich nicht langweilig oder bedrohlich fachlich wirken.
Die Eigenschaften nach Relevanz für uns geordnet sind:
1. Modern
2. Sachlich
3. Nüchtern, nicht zu bunt
4. Erfrischend (im Sinne von nicht langweilig)
5. Hochwertig
6. Luftig
Uns als Redaktion geht es zudem darum, dass wir ein Cover bekommen, dass den Inhalt des Buches wiedergibt. Wir wollen jährlich den Titel auswechseln können, ohne dass sich Text und Bild dabei beißen.
Zur Ausschreibung gehört neben dem Buchcover auch der Buchrücken und die Rückseite des Buchdeckels. Im Anhang haben wir das Cover aus dem Buch des letzten Jahres angefügt, sowie unser Verlags-Logo.

```html
<!DOCTYPE html>
<html lang="de">
<head>
<meta charset="utf-8">
<title>Merkurpfade – Oktober 2021</title>
<link rel="stylesheet" href="https://fonts.googleapis.com/css2?family=Inter:wght@200;300;400;700;800&display=swap">
<style>
  :root {
    --navy: #19213f;
    --blue-mid: #1d4a86;
    --blue-deep: #1a5f98;
    --signal-red: #c61a3c;
    --white: #ffffff;
    --paper: #ffffff;
  }
  * { margin: 0; padding: 0; box-sizing: border-box; }
  html, body { width: 845px; height: 1200px; overflow: hidden; background: var(--paper); }
  body { font-family: "Inter", "Helvetica Neue", Arial, sans-serif; color: var(--white); }

  .cover { position: relative; width: 845px; height: 1200px; background: var(--paper); overflow: hidden; }

  .cover-visual {
    position: absolute; left: 0; top: 0; width: 845px; height: 1043px;
    background:
      radial-gradient(ellipse at 30% 80%, rgba(40,150,210,0.45), transparent 60%),
      linear-gradient(180deg, var(--navy) 0%, #1d3565 35%, var(--blue-mid) 65%, var(--blue-deep) 100%);
  }

  .series-title { position: absolute; left: 45px; width: 752px; display: flex; justify-content: space-between; line-height: 1; }
  .series-title--top { top: 44px; font-size: 158px; font-weight: 400; }
  .series-title--bottom { top: 194px; font-size: 121px; font-weight: 200; }

  .headline-box {
    position: absolute; left: 262px; top: 365px; width: 583px; height: 219px;
    background: var(--signal-red);
    display: flex; align-items: center; justify-content: flex-end;
    padding-right: 43px;
  }
  .headline { font-size: 61px; font-weight: 400; line-height: 1.4; text-align: right; letter-spacing: -0.5px; }

  .edition-month { position: absolute; left: 612px; top: 850px; font-size: 57px; font-weight: 400; line-height: 1; }
  .edition-year { position: absolute; left: 612px; top: 912px; height: 100px; }
  .edition-year__century {
    position: absolute; left: 0; top: 0; width: 62px; height: 100px;
    display: flex; align-items: center; justify-content: center;
  }
  .edition-year__century span {
    display: block; transform: rotate(-90deg); font-size: 62px; font-weight: 200; line-height: 1;
  }
  .edition-year__decade { position: absolute; left: 66px; top: -14px; font-size: 128px; font-weight: 300; line-height: 1; letter-spacing: -3px; }

  .editors { position: absolute; left: 45px; top: 987px; font-size: 21px; font-weight: 700; }

  .accent-stripe { position: absolute; left: 0; top: 1043px; width: 800px; height: 15px; background: var(--signal-red); }

  .publisher { position: absolute; left: 486px; top: 1088px; display: flex; align-items: center; gap: 18px; }
  .publisher__dot { width: 66px; height: 66px; border: 3px solid var(--signal-red); border-radius: 50%; }
  .publisher__name { font-size: 33px; font-weight: 800; color: var(--signal-red); letter-spacing: 0.5px; }
</style>
</head>
<body>
<main class="cover">
  <div class="cover-visual" role="img" aria-label="Börsengrafik mit Kerzen- und Balkendiagramm vor einer gepunkteten Weltkarte in Blautönen"></div>

  <h1 aria-label="Merkurpfade">
    <span class="series-title series-title--top" aria-hidden="true"><span>M</span><span>E</span><span>R</span><span>K</span><span>U</span><span>R</span></span>
    <span class="series-title series-title--bottom" aria-hidden="true"><span>P</span><span>F</span><span>A</span><span>D</span><span>E</span></span>
  </h1>

  <div class="headline-box">
    <h2 class="headline">Der Zins kehrt<br>langsam zurück</h2>
  </div>

  <div class="edition-month">Oktober</div>
  <div class="edition-year" aria-label="2021">
    <div class="edition-year__century" aria-hidden="true"><span>20</span></div>
    <div class="edition-year__decade" aria-hidden="true">21</div>
  </div>

  <p class="editors">Tom Wegscheid | Jonas Brandtner (Hg.)</p>

  <div class="accent-stripe"></div>

  <div class="publisher">
    <div class="publisher__dot"></div>
    <span class="publisher__name">FALKENBLATT</span>
  </div>
</main>
</body>
</html>
```